Brightwell Power Systems

We'd like a web design that's beautiful and professional. We replace existing inefficient systems (mostly lighting at the moment but expanding) with highly efficient systems.

```html
<!DOCTYPE html>
<html lang="en">
<head>
<meta charset="utf-8">
<title>Brightwell Power Systems – LED Lighting Solutions</title>
<link href="https://fonts.googleapis.com/css2?family=Pathway+Gothic+One&display=swap" rel="stylesheet">
<style>
:root{
  --green:#00c159;
  --green-dark:#019a47;
  --ink:#111111;
  --grey-text:#8a8a8a;
  --footer-bg:#efefef;
  --footer-text:#9a9a9a;
  --border:#dddddd;
  --white:#ffffff;
}
*{box-sizing:border-box;margin:0;padding:0}
html,body{width:1193px;height:1200px;overflow:hidden;background:var(--white)}
body{position:relative;font-family:"Pathway Gothic One",sans-serif;color:var(--ink)}
a{color:inherit;text-decoration:none}

.site-header{position:absolute;left:0;top:0;width:1193px;height:44px;border-top:3px solid var(--green);border-bottom:1px solid #cfcfcf;background:var(--white);z-index:3}
.brand{position:absolute;left:100px;top:8px;width:92px;height:76px;background:var(--white);border:1px solid #bbb;display:flex;flex-direction:column;align-items:center;justify-content:center;gap:4px;color:var(--green-dark);font-size:14px;line-height:1.05;text-align:center;z-index:4}
.brand-mark{width:22px;height:22px;background:var(--green)}
.main-nav{position:absolute;left:340px;top:9px;display:flex;font-size:17px;color:var(--green-dark)}
.main-nav a{padding:0 28px}
.main-nav a+a{border-left:1px solid var(--green-dark)}
.main-nav a:first-child{padding-left:6px;padding-right:31px}
.phone-tab{position:absolute;left:832px;top:0;width:264px;height:38px;color:var(--white);font-size:19px;display:flex;align-items:center;gap:8px;padding-left:34px}
.phone-tab svg.tab-bg{position:absolute;left:0;top:0;z-index:-1}

.hero{position:absolute;left:0;top:45px;width:1193px;height:670px;
  background:
    radial-gradient(ellipse 14% 24% at 42% 45%,rgba(0,0,0,.95) 0%,rgba(0,0,0,.9) 55%,rgba(0,0,0,0) 100%),
    radial-gradient(ellipse 26% 36% at 42% 42%,rgba(220,120,200,.55) 0%,rgba(120,200,150,.35) 45%,rgba(0,0,0,0) 75%),
    radial-gradient(ellipse 70% 80% at 42% 45%,#6a4cc8 0%,#4a30b0 40%,#3a2596 65%,#2a1a6e 100%)}
.hero-arrow{position:absolute;top:258px}
.hero-arrow.prev{left:68px}
.hero-arrow.next{left:1098px}

.hero-panel{position:absolute;left:100px;top:495px;width:1000px;height:202px;background:var(--ink)}
.hero-panel::before{content:"";position:absolute;left:0;right:0;top:13px;border-top:1px dashed var(--green)}
.hero-title{position:absolute;left:17px;top:30px;line-height:.9;font-weight:400}
.hero-title .line1{display:block;font-size:55px;color:var(--white)}
.hero-title .line2{display:block;font-size:90px;color:var(--green)}
.hero-tagline{position:absolute;left:671px;top:60px;width:320px;font-size:25.5px;line-height:1.12;color:#6b6b6b}

.featured-bar{position:absolute;left:100px;top:697px;width:1000px;height:41px;background:var(--green);color:var(--white);font-size:19px;padding:7px 15px}

.products{position:absolute;left:100px;top:748px;width:1000px;display:flex;justify-content:space-between}
.product-card{width:191px;height:227px;border:1px solid var(--border);background:var(--white);position:relative;text-align:center}
.product-card h3{font-weight:400;font-size:21px;color:#555;margin-top:4px}
.product-shot{position:absolute;left:8px;top:29px;width:173px;height:175px;border:1px solid #eee;background:var(--white)}
.shot-bulb{background:radial-gradient(ellipse 22% 36% at 50% 42%,#e8e8e8 0%,#c9ccce 60%,rgba(255,255,255,0) 100%),var(--white)}
.shot-worklights{background:radial-gradient(ellipse 34% 32% at 50% 45%,#3a3a3a 0%,#4f8f3a 55%,rgba(255,255,255,0) 100%),var(--white)}
.shot-spot{background:radial-gradient(ellipse 32% 30% at 52% 42%,#7a6a5a 0%,#c6c9cc 45%,rgba(255,255,255,0) 100%),var(--white)}
.shot-fixture{background:radial-gradient(ellipse 34% 34% at 52% 45%,#dcdcdc 0%,#3a3a3a 55%,rgba(255,255,255,0) 100%),var(--white)}
.shot-highbay{background:radial-gradient(ellipse 36% 34% at 55% 42%,#e4e8f0 0%,#aab0bc 55%,rgba(255,255,255,0) 100%),var(--white)}
.learn-more{position:absolute;left:50%;transform:translateX(-50%);top:192px;background:var(--green);color:var(--white);font-size:15px;padding:2px 12px;border-radius:2px;border:1px solid var(--green-dark);white-space:nowrap}
.carousel-btn{position:absolute;top:832px}
.carousel-btn.prev{left:60px}
.carousel-btn.next{left:1104px}

.intro-copy{position:absolute;left:100px;top:991px;width:660px;font-size:16px;line-height:1.18;color:var(--grey-text)}

.site-footer{position:absolute;left:0;top:1080px;width:1193px;height:120px;background:var(--footer-bg);border-top:1px solid #dcdcdc}
.footer-links{position:absolute;top:8px;list-style:none;font-size:15px;line-height:18px;color:var(--footer-text)}
.footer-links.col1{left:111px}
.footer-links.col2{left:310px}
.footer-links.col3{left:540px}
.help-box{position:absolute;left:792px;top:-13px;width:306px;height:60px}
.help-box .label{position:absolute;left:22px;top:15px;font-size:26px;color:var(--white);white-space:nowrap}
.follow{position:absolute;left:812px;top:55px;display:flex;align-items:center;gap:10px;font-size:16px;color:var(--footer-text)}
.follow .rule{width:94px;border-top:1px solid #bbb;margin-right:6px}
.social-dot{width:27px;height:27px;border-radius:50%;background:#6cc24a}
.social-dot+.social-dot{margin-left:4px}
</style>
</head>
<body>

<header class="site-header">
  <div class="brand"><span class="brand-mark"></span>Brightwell Power Systems</div>
  <nav class="main-nav">
    <a href="#">HOME</a><a href="#">WHY LED?</a><a href="#">CASE STUDIES</a><a href="#">FAQ</a><a href="#">ENERGY AUDIT</a>
  </nav>
  <div class="phone-tab">
    <svg class="tab-bg" width="264" height="38"><path d="M0 0H264L256 34Q255 38 250 38H14Q9 38 8 34Z" fill="#00b452"/></svg>
    <svg width="14" height="20" viewBox="0 0 14 20"><path d="M4 1 L7 5 L5 7 Q6 11 9 13 L11 11 L14 15 L11 18 Q4 16 1 6 Z" fill="#fff"/></svg>
    1-800-555-0142
  </div>
</header>

<section class="hero" role="img" aria-label="Photo of a walk-through tunnel made of arched strings of colourful LED lights at night">
  <svg class="hero-arrow prev" width="32" height="72"><path d="M28 2 L6 36 L28 70" stroke="#ddd" stroke-width="7" fill="none"/></svg>
  <svg class="hero-arrow next" width="32" height="72"><path d="M4 2 L26 36 L4 70" stroke="#ddd" stroke-width="7" fill="none"/></svg>
</section>

<div class="hero-panel">
  <h1 class="hero-title"><span class="line1">LED LIGHTING</span><span class="line2">SOLUTIONS</span></h1>
  <p class="hero-tagline">Leadership in Energy &amp; Environmental Design LED products available on GSA Schedule - GS-00X-1234A</p>
</div>

<div class="featured-bar">FEATURED LED PRODUCTS</div>

<section class="products">
  <article class="product-card"><h3>FREE LIGHTING AUDIT</h3><div class="product-shot shot-bulb" role="img" aria-label="Product photo of a white LED light bulb"></div><a class="learn-more" href="#">LEARN MORE</a></article>
  <article class="product-card"><h3>THE ADVANTAGE</h3><div class="product-shot shot-worklights" role="img" aria-label="Product photo of portable black and green LED work lights"></div><a class="learn-more" href="#">LEARN MORE</a></article>
  <article class="product-card"><h3>LED SYSTEM TOOLS</h3><div class="product-shot shot-spot" role="img" aria-label="Product photo of a silver LED spotlight lamp"></div><a class="learn-more" href="#">LEARN MORE</a></article>
  <article class="product-card"><h3>LED LIGHTING FIXTURES</h3><div class="product-shot shot-fixture" role="img" aria-label="Product photo of a round black LED flood light fixture"></div><a class="learn-more" href="#">LEARN MORE</a></article>
  <article class="product-card"><h3>FREE LIGHTING AUDIT</h3><div class="product-shot shot-highbay" role="img" aria-label="Product photo of a large LED high bay lamp"></div><a class="learn-more" href="#">LEARN MORE</a></article>
</section>
<svg class="carousel-btn prev" width="36" height="36"><circle cx="18" cy="18" r="16" fill="#fff" stroke="#00c159" stroke-width="3"/><path d="M21 10 L13 18 L21 26" stroke="#00c159" stroke-width="4" fill="none"/></svg>
<svg class="carousel-btn next" width="36" height="36"><circle cx="18" cy="18" r="16" fill="#fff" stroke="#00c159" stroke-width="3"/><path d="M15 10 L23 18 L15 26" stroke="#00c159" stroke-width="4" fill="none"/></svg>

<p class="intro-copy">Our world-class engineers combine the best available components with innovative optical, electrical and thermal designs to create LED commercial lamps and lighting systems that are optimized for superior performance. We are superbly positioned to continue as an industry-leading innovator for years to come.</p>

<footer class="site-footer">
  <ul class="footer-links col1"><li>LED</li><li>HID</li><li>LINEAR FLUORESCENT</li><li>CFL NON INTEGRATED</li><li>HALOGEN</li><li>SEE ALL TECHNOLOGIES</li></ul>
  <ul class="footer-links col2"><li>WHERE TO BUY</li><li>PRESSROOM</li><li>NORTHLUME GRID</li><li>CORVANE LIGHTING</li><li>ABOUT HALCYON LIGHTING</li><li>SITE MAP</li></ul>
  <ul class="footer-links col3"><li>PRIVACY POLICY</li><li>COOKIE DISCLOSURE</li><li>ACCESSIBILITY STATEMENT</li><li>TERMS OF USE</li><li>TERMS OF SALE</li></ul>
  <div class="help-box">
    <svg width="306" height="60"><path d="M0 13 L10 0 L10 13 Z M306 13 L296 0 L296 13 Z" fill="#019a47"/><rect x="10" y="0" width="286" height="58" fill="#00c159"/><circle cx="251" cy="31" r="16" fill="none" stroke="#111" stroke-width="3"/><text x="251" y="40" text-anchor="middle" font-family="Pathway Gothic One, sans-serif" font-size="24" fill="#111">?</text></svg>
    <span class="label">QUESTIONS ?&nbsp; LET US HELP.</span>
  </div>
  <div class="follow">FOLLOW US AT <span class="rule"></span><span class="social-dot"></span><span class="social-dot"></span></div>
</footer>

</body>
</html>
```